Vornix 1デザイン(2サイズ)
Kelpa 1デザイン(2サイズ)
TALLWIRE 1デザイン(2サイズ)

6つのバナーですが、デザインは3種類(各2サイズ)で、作成をお願いします。

3つの掲載先(Vornix、Kelpa、Tallwire)を検討しています。
3つの広告は、デザインを違うものでお願いします。

リンク先のランディングページをつながるデザインでお願いします。
https://kmt-qs.jp/opt-in/

参考のために、母体となるサイトのURLも記載します。
https://kmt-qs.jp/

素材は、購入してください。
こちらから、データ提供できるものはございません。
デザイナーと連絡が取れなくなってしまって、元データがありません。
グラフデータなどもランディングページ内にあるものを作成してください。

どうそ、よろしくお願いいたします。

定期的なhtmlメルマガなどの作成ができる方など、継続的にお願いできる方だとありがたいです。
細かなこだわりはないので、提案をくださるかた、スピーディーにたたき台を作成していただける方、自主的に進めてくれる方を探しております。
強調したいポイント(すべてを入れていただく必要はありません)
・売上アップ
・300万円の助成金
・離職を減らす
・塾の経営
・国に頼らない

というキーワードを出したいです。

あと、売上アップのグラフなど(ランディングページ内)。
• 添付ファイル参照
シンプル 複雑
単色 カラフル
暗い 明るい
日常 高級
遊び心 厳粛
未来的 伝統的
女性的 男性的
• 高解像度JPG (.jpg)
• イラストレーター形式 (.ai)
• フォトショップ形式 (.psd)
• PNG形式 (.png)
サイズは添付ファイルに記載しております。

```html
<!DOCTYPE html>
<html lang="ja">
<head>
<meta charset="utf-8">
<title>VR&オンライン指導 バナー</title>
<link rel="stylesheet" href="https://fonts.googleapis.com/css2?family=M+PLUS+Rounded+1c:wght@500;700;800&display=swap">
<style>
  :root {
    --pink: #f591b5;
    --pink-deep: #ee5f95;
    --pink-text: #e9558c;
    --white: #ffffff;
    --cream: #fde7b6;
    --box-line: #d9d9d9;
    --bar-green: #8cc43f;
    --bar-gray: #cfcfcf;
    --arrow-red: #ea3b3b;
    --axis: #bdbdbd;
    --photo-dark: #4a4a4a;
    --photo-light: #e9e9ea;
  }
  * { margin: 0; padding: 0; box-sizing: border-box; }
  html, body { width: 675px; height: 1200px; overflow: hidden; background: var(--white); }
  .banner {
    position: relative;
    width: 675px;
    height: 1200px;
    overflow: hidden;
    font-family: "M PLUS Rounded 1c", sans-serif;
    background: linear-gradient(to bottom, var(--white) 0, var(--white) 590px, var(--cream) 760px, var(--cream) 100%);
  }
  .hero-band { position: absolute; left: 0; top: 0; width: 675px; height: 420px; }
  .headset-photo {
    position: absolute; left: 90px; top: 0; width: 530px; height: 326px;
    border-radius: 0 0 60px 60px;
    background: linear-gradient(160deg, var(--photo-light) 0%, var(--white) 40%, var(--photo-dark) 75%, #2c2c2c 100%);
  }
  .headline {
    position: absolute; left: 0; top: 395px; width: 675px;
    text-align: center; color: var(--pink-text); font-weight: 800; line-height: 1.25;
  }
  .headline .line-1 { font-size: 40px; }
  .headline .line-2 { font-size: 46px; letter-spacing: 2px; }
  .headline small { font-size: 28px; }
  .benefits {
    position: absolute; top: 558px; left: 76px; width: 523px;
    display: flex; justify-content: space-between; list-style: none;
  }
  .benefits li {
    width: 156px; height: 106px; background: var(--white);
    border: 2px solid var(--box-line);
    display: flex; align-items: center; justify-content: center; text-align: center;
    color: var(--pink-text); font-size: 23px; font-weight: 700; line-height: 1.35;
  }
  .growth-chart { position: absolute; left: 0; top: 0; width: 675px; height: 1200px; }
  .child-photo {
    position: absolute; left: -5px; top: 941px; width: 234px; height: 234px;
    border-radius: 50%; border: 6px solid var(--pink);
    background: radial-gradient(circle at 55% 40%, #f3d6c4 0%, #b9a79a 45%, #6b6b6b 100%);
  }
</style>
</head>
<body>
<div class="banner">
  <svg class="hero-band" viewBox="0 0 675 420" aria-hidden="true">
    <path d="M0 0H675V330C560 300 470 330 380 355C250 392 120 395 0 370Z" fill="var(--pink)"/>
  </svg>
  <div class="headset-photo" role="img" aria-label="白と黒のVRヘッドセットの写真"></div>

  <h1 class="headline">
    <span class="line-1">VR&amp;オンライン指導<small>による</small></span><br>
    <span class="line-2">新しいサービス<small>で</small></span>
  </h1>

  <ul class="benefits">
    <li>売上<br>アップ</li>
    <li>離職を<br>減らす</li>
    <li>国に頼らない<br>塾の経営</li>
  </ul>

  <svg class="growth-chart" viewBox="0 0 675 1200" aria-label="売上アップを示す棒グラフ" role="img">
    <defs>
      <linearGradient id="arrowFade" x1="0" y1="1" x2="0" y2="0">
        <stop offset="0" stop-color="var(--arrow-red)" stop-opacity="0.15"/>
        <stop offset="0.6" stop-color="var(--arrow-red)" stop-opacity="0.85"/>
        <stop offset="1" stop-color="var(--arrow-red)"/>
      </linearGradient>
    </defs>
    <line x1="311" y1="705" x2="311" y2="1166" stroke="var(--axis)" stroke-width="2"/>
    <line x1="331" y1="711" x2="518" y2="711" stroke="#333" stroke-width="2" stroke-dasharray="10 7"/>
    <rect x="342" y="1012" width="92" height="57" fill="var(--bar-green)"/>
    <rect x="342" y="1069" width="92" height="97" fill="var(--bar-gray)"/>
    <rect x="518" y="711" width="94" height="257" fill="var(--bar-green)"/>
    <rect x="518" y="968" width="94" height="198" fill="var(--bar-gray)"/>
    <path d="M388 720L436 799H408V1005H368V799H340Z" fill="url(#arrowFade)"/>
  </svg>

  <div class="child-photo" role="img" aria-label="VRゴーグルを着けた子どもの写真"></div>
</div>
</body>
</html>
```